2018 Fundraiser Event Flier

We are a non profit that works in the homeless community, The Lanternwick Guild. We offer a unique program of supported employment that is all about community engagement and building relationships not only with our participants but with community businesses and non profit partners. Our mission statement is "We seek and foster partnerships between the business and nonprofit communities to respectfully and effectively guide individuals from disenfranchised communities forward in sustainable employment to realize their potential of fully enriched lives for themselves and their families" We are having a fundraising event on Dec 13 and need a flier to advertise the event both via email and physical postings. We like a black background and bright colors (see uploaded example) and want to advertise the event and a small amount about who we are. Fun and bright. We will upload two of our logos and two photos that we have used in branding previously.

```html
<!DOCTYPE html>
<html lang="en">
<head>
<meta charset="utf-8">
<title>The Lanternwick Guild – Fundraiser Event</title>
<link rel="stylesheet" href="https://fonts.googleapis.com/css2?family=Abril+Fatface&family=Oswald:wght@600&family=Lato:wght@400;700&display=swap">
<style>
  :root {
    --stage: #8c8c8c;
    --ink: #000000;
    --paper: #ffffff;
    --green: #22ee33;
    --green-dark: #10c622;
    --yellow: #fff200;
    --magenta: #f50ff0;
    --photo-light: #d2d2d2;
    --photo-mid: #7a7a7a;
    --photo-dark: #262626;
  }
  * { box-sizing: border-box; margin: 0; padding: 0; }
  html, body { width: 1200px; height: 1200px; overflow: hidden; }
  body { background: var(--stage); font-family: "Lato", sans-serif; }

  .flier {
    position: absolute; left: 190px; top: 30px;
    width: 820px; height: 1140px;
    background: var(--ink); overflow: hidden;
  }

  .hero-photo {
    position: absolute; left: 0; top: 0; width: 820px; height: 560px;
    background:
      linear-gradient(to bottom, rgba(0,0,0,0) 60%, var(--ink) 100%),
      radial-gradient(ellipse 22% 26% at 42% 66%, var(--photo-light) 0%, rgba(210,210,210,0) 100%),
      radial-gradient(ellipse 16% 14% at 40% 28%, #9c9c9c 0%, rgba(156,156,156,0) 100%),
      linear-gradient(to right, #3a3a3a 0%, #6e6e6e 30%, #555555 55%, #4a4a4a 80%, #2e2e2e 100%);
  }

  .brand-badge { position: absolute; left: 571px; top: 0; width: 213px; height: 222px; }
  .brand-badge svg { position: absolute; inset: 0; }
  .brand-badge .badge-name {
    position: absolute; left: 12px; right: 12px; top: 100px;
    text-align: center; font-family: "Lato", sans-serif; font-weight: 700;
    font-size: 24px; line-height: 1.15; color: var(--ink); text-transform: uppercase;
  }

  .event-title {
    position: absolute; left: 0; width: 820px; top: 518px;
    text-align: center; font-family: "Abril Fatface", serif; font-weight: 400;
    font-size: 74px; color: var(--paper); letter-spacing: 6px; white-space: nowrap;
  }

  .date-ribbon { position: absolute; left: 90px; top: 629px; width: 640px; height: 102px; }
  .date-ribbon svg { position: absolute; inset: 0; }
  .date-ribbon .date {
    position: absolute; left: 55px; width: 514px; top: 0; height: 87px;
    display: flex; align-items: center; justify-content: center;
    font-family: "Oswald", sans-serif; font-weight: 600; font-size: 76px;
    letter-spacing: -2px; color: var(--ink);
  }

  .mission-tag { position: absolute; left: 0; top: 770px; width: 302px; height: 51px; }
  .mission-tag svg { position: absolute; inset: 0; }
  .mission-tag span {
    position: absolute; left: 35px; top: 4px;
    font-family: "Abril Fatface", serif; font-size: 30px; letter-spacing: 1px; color: var(--ink);
  }

  .mission-text {
    position: absolute; left: 35px; top: 838px; width: 356px;
    font-size: 19.2px; line-height: 25px; color: var(--paper); text-align: justify;
  }

  .website {
    position: absolute; left: 36px; top: 1062px;
    font-size: 20px; letter-spacing: 3.6px; color: var(--paper); font-weight: 700;
  }

  .quote-photo {
    position: absolute; left: 454px; top: 794px; width: 345px; height: 193px;
    border: 3px solid #d8d8d8;
    background: linear-gradient(to bottom, #a9a9a9 0%, #8c8c8c 60%, #4a4a4a 100%);
  }

  .partner-mark { position: absolute; left: 454px; top: 1010px; width: 92px; height: 91px; background: var(--paper); }

  .guild-mark {
    position: absolute; left: 581px; top: 1010px; width: 206px; height: 92px;
    background: var(--paper); display: flex; align-items: center; justify-content: center;
    text-align: center; font-family: "Lato", sans-serif; font-weight: 700;
    font-size: 22px; line-height: 1.1; color: var(--ink); text-transform: uppercase;
  }

  .footer-band { position: absolute; left: 0; top: 1115px; width: 820px; height: 25px; background: var(--magenta); }
</style>
</head>
<body>
  <main class="flier">
    <div class="hero-photo" role="img" aria-label="Black and white photo of a man in a knit hat holding a cardboard sign reading Willing to Work"></div>

    <div class="brand-badge">
      <svg width="213" height="222" viewBox="0 0 213 222">
        <polygon points="0,0 213,0 213,198 106.5,222 0,198" fill="#ffffff"/>
      </svg>
      <div class="badge-name">The Lanternwick Guild</div>
    </div>

    <h1 class="event-title">Fundraiser Event</h1>

    <div class="date-ribbon">
      <svg width="640" height="102" viewBox="0 0 640 102">
        <polygon points="0,25 75,25 75,102 7,102 30,62" fill="#10c622"/>
        <polygon points="640,25 565,25 565,102 633,102 610,62" fill="#10c622"/>
        <rect x="55" y="0" width="514" height="87" fill="#22ee33"/>
      </svg>
      <div class="date">Dec 13 2018</div>
    </div>

    <div class="mission-tag">
      <svg width="302" height="51" viewBox="0 0 302 51">
        <polygon points="0,0 284,0 302,25.5 284,51 0,51" fill="#fff200"/>
      </svg>
      <span>Our mission</span>
    </div>

    <p class="mission-text">We seek and foster partnerships between the business and nonprofit communities to respectfully and effectively guide individuals from disenfranchised communities forward in sustainable employment to realize their potential of fully enriched lives for themselves and their families</p>

    <p class="website">www.brightpathalliance.org</p>

    <div class="quote-photo" role="img" aria-label="Street photo of a person sleeping against a wall, with a quote about overcoming poverty"></div>

    <div class="partner-mark" role="img" aria-label="Partner organisation mark"></div>
    <div class="guild-mark">The Lanternwick Guild</div>

    <div class="footer-band"></div>
  </main>
</body>
</html>
```